Email Design Creative Design Needed

Our website is called CampusLedger.org. One of our competitor(varsity scout.us.com) is using the following email creative.
http://pqr.brightquill.com/Affiliate/Assets/3532.html
http://pqr.brightquill.com/Affiliate/Assets/7921.html
http://pqr.brightquill.com/Affiliate/Assets/8061.html

We would like to use similar email creative without copying their exact creative. You can use the above as a guide but then come up with your own version of the creative.
The above are just concepts, please be creative and come up with your own version of it, without feeling that they have been copied. Feel free to move the components around. Also, feel free to change the colours and text.

Please find attached the CampusLedger.org logo.

Reason: We would like to receive more designs.

College

```html
<!DOCTYPE html>
<html lang="en">
<head>
<meta charset="utf-8">
<title>CampusLedger – Careers in Education</title>
<link href="https://fonts.googleapis.com/css2?family=Poppins:wght@500;600&family=Source+Sans+3:wght@400;600;700&display=swap" rel="stylesheet">
<style>
  :root {
    --page-bg: #eef1f7;
    --indigo: #23305e;
    --indigo-soft: #34457f;
    --coral: #ef6c4a;
    --coral-dark: #d4532f;
    --sun: #ffc857;
    --card: #ffffff;
    --row-alt: #f5f7fc;
    --rule: #dfe4ef;
    --text-main: #2c3345;
    --text-muted: #5a6275;
    --photo-warm: #f0b27a;
    --photo-light: #f7e6d3;
  }
  * { margin: 0; padding: 0; box-sizing: border-box; }
  html, body { width: 1200px; height: 800px; overflow: hidden; }
  body {
    position: relative;
    background: var(--page-bg);
    font-family: "Source Sans 3", Arial, sans-serif;
    color: var(--text-main);
  }

  .topbar {
    position: absolute; top: 0; left: 0; width: 1200px; height: 56px;
    background: var(--indigo);
  }
  .brand {
    position: absolute; left: 300px; top: 0; height: 56px;
    display: flex; align-items: center; gap: 10px;
  }
  .brand-mark { width: 18px; height: 18px; background: var(--sun); }
  .brand-name {
    font-family: "Poppins", sans-serif; font-weight: 600; font-size: 21px;
    color: #fff;
  }
  .topbar-tag {
    position: absolute; right: 300px; top: 0; height: 56px;
    display: flex; align-items: center;
    font-size: 13px; font-weight: 600; letter-spacing: 1.2px;
    text-transform: uppercase; color: var(--sun);
  }

  .hero {
    position: absolute; top: 56px; left: 300px; width: 600px; height: 240px;
    display: flex;
  }
  .hero-copy {
    width: 320px; height: 240px; padding: 30px 28px 0;
    background: linear-gradient(150deg, var(--coral) 0%, var(--coral-dark) 100%);
    color: #fff;
  }
  .hero-title {
    font-family: "Poppins", sans-serif; font-weight: 600;
    font-size: 23px; line-height: 30px;
  }
  .hero-sub { margin-top: 10px; font-size: 14px; line-height: 19px; }
  .hero-button {
    margin-top: 18px; display: inline-block;
    padding: 10px 22px; border-radius: 22px;
    background: var(--indigo); color: #fff;
    font-family: "Poppins", sans-serif; font-weight: 500; font-size: 13px;
  }
  .hero-photo {
    width: 280px; height: 240px;
    background: linear-gradient(200deg, var(--photo-light) 0%, var(--photo-warm) 60%, #c9865a 100%);
  }

  .careers {
    position: absolute; top: 312px; left: 300px; width: 600px; height: 262px;
    background: var(--card);
    border-top: 4px solid var(--sun);
    box-shadow: 0 2px 8px rgba(35, 48, 94, 0.08);
  }
  .careers-head, .career-row {
    display: flex; align-items: center; padding: 0 20px;
  }
  .careers-head {
    height: 32px; background: var(--indigo-soft); color: #fff;
    font-family: "Poppins", sans-serif; font-weight: 500; font-size: 12.5px;
  }
  .col-role { width: 290px; }
  .col-pay { width: 150px; }
  .col-explore { width: 120px; text-align: right; }
  .career-row {
    height: 45px; border-bottom: 1px solid var(--rule);
    font-size: 13.5px; line-height: 17px;
  }
  .career-row:last-child { border-bottom: 0; }
  .career-row:nth-child(odd) { background: var(--row-alt); }
  .career-row .col-pay { font-weight: 700; color: var(--indigo); }
  .career-row .col-explore { font-weight: 600; color: var(--coral-dark); }

  .fine-print {
    position: absolute; top: 592px; left: 300px; width: 600px;
    text-align: center; font-size: 11.5px; line-height: 16px;
    color: var(--text-muted);
  }
  .fine-print p { margin-bottom: 9px; }
  .fine-print .unsubscribe { color: var(--coral-dark); text-decoration: underline; }
  .fine-print .divider { border-top: 1px solid var(--rule); margin: 4px 0 9px; }
  .fine-print .copyright { margin-bottom: 0; color: var(--indigo); font-weight: 600; }
</style>
</head>
<body>
  <header class="topbar">
    <div class="brand">
      <span class="brand-mark"></span>
      <span class="brand-name">CampusLedger</span>
    </div>
    <div class="topbar-tag">Education &amp; Teaching</div>
  </header>

  <section class="hero">
    <div class="hero-copy">
      <h1 class="hero-title">Start Your Teaching Career Online or On Campus</h1>
      <p class="hero-sub">Compare education degree programs side by side.</p>
      <span class="hero-button">Compare Teaching Degrees</span>
    </div>
    <div class="hero-photo" role="img" aria-label="Photo of a teacher guiding a young student with schoolwork"></div>
  </section>

  <section class="careers">
    <div class="careers-head">
      <span class="col-role">Career Path</span>
      <span class="col-pay">Median Pay*</span>
      <span class="col-explore">Explore</span>
    </div>
    <div class="career-rows">
      <div class="career-row">
        <span class="col-role">Preschool &amp; Childcare Center Directors</span>
        <span class="col-pay">$51,290 / yr</span>
        <span class="col-explore">See programs ›</span>
      </div>
      <div class="career-row">
        <span class="col-role">Education Administrators</span>
        <span class="col-pay">$90,200 / yr</span>
        <span class="col-explore">See programs ›</span>
      </div>
      <div class="career-row">
        <span class="col-role">Elementary &amp; Secondary School Leaders</span>
        <span class="col-pay">$90,200 / yr</span>
        <span class="col-explore">See programs ›</span>
      </div>
      <div class="career-row">
        <span class="col-role">School, Guidance &amp; Vocational Counselors</span>
        <span class="col-pay">$56,540 / yr</span>
        <span class="col-explore">See programs ›</span>
      </div>
      <div class="career-row">
        <span class="col-role">Preschool Teachers</span>
        <span class="col-pay">$30,150 / yr</span>
        <span class="col-explore">See programs ›</span>
      </div>
    </div>
  </section>

  <footer class="fine-print">
    <p>*Median pay figures from the U.S. Bureau of Labor Statistics.</p>
    <p>Financial aid is available to those who qualify; eligibility is confirmed by a partner school representative. Outcomes vary by institution and program, and employment is not guaranteed.</p>
    <p>To stop receiving these emails, <span class="unsubscribe">unsubscribe</span> or write to Bright Quill Marketing Inc, PO Box 514427 #27714, Springfield, IL 62701-4427.</p>
    <div class="divider"></div>
    <p class="copyright">Copyright © CampusLedger.org · All rights reserved.</p>
  </footer>
</body>
</html>
```